need corporate, modern business card created for Consulting Company

I need a slick business card using elements from my website, as well as, integrating my pixelharbor-created logo (see files).

The business card needs to be:
1. Corporate and modern
2. Clean and professional

I've included a PSD with the logo/icon that you can use to create it. Feel free to try a metallic finish on the logo, make it bigger/small, underlay it. Whatever you need to do to make my card stand out.

Try a black background, or white background or gray.

The idea is for my card to be memorable as well as professional and corporate.

Target Market(s)

Corporate business in the US and Canada.

Industry/Entity Type

Business

Contact Information for Business Card

Business Leveraging Technology
Malcolm Tudd, Senior Partner
office: 1 877 555 0143
mobile: 1 519 555 0172
website: http://www.vextorial.com

Requirements
Must have
• Card-related information
• corporate, yet modern
• clean and professional
• incorporate the icon only
• must have an editable form when complete!
Nice to have
• metallic icon might be cool
• try it with white or black

```html
<!DOCTYPE html>
<html lang="en">
<head>
<meta charset="utf-8">
<title>Vextorial Business Card</title>
<link href="https://fonts.googleapis.com/css2?family=Exo+2:wght@400;500;600&display=swap" rel="stylesheet">
<style>
  :root {
    --page: #d9d9d9;
    --card: #252526;
    --blue: #3c74cf;
    --blue-light: #6d9ae6;
    --white: #f2f2f2;
    --grey: #8a8a8a;
    --grey-dim: #5a5a5a;
  }
  * { box-sizing: border-box; margin: 0; padding: 0; }
  html, body { width: 1200px; height: 898px; overflow: hidden; background: var(--page); }
  body { font-family: "Exo 2", sans-serif; position: relative; }

  .card {
    position: absolute;
    top: 289px;
    width: 540px;
    height: 320px;
    background: var(--card);
    border-radius: 30px;
    box-shadow: 0 8px 22px rgba(0,0,0,.25);
    overflow: hidden;
  }
  .card--front { left: 40px; }
  .card--back { left: 620px; }

  .card__frame {
    position: absolute;
    inset: 14px;
    border: 2px solid var(--blue);
    border-radius: 24px;
  }

  .band {
    position: absolute;
    left: 0;
    top: 78px;
    width: 290px;
    height: 36px;
    background: var(--blue);
    border: 2px solid var(--blue-light);
    border-left: none;
    border-radius: 0 18px 18px 0;
  }
  .tab {
    position: absolute;
    right: 0;
    top: 26px;
    width: 62px;
    height: 34px;
    background: var(--blue);
    border: 2px solid var(--blue-light);
    border-right: none;
    border-radius: 17px 0 0 17px;
  }

  .identity { position: absolute; left: 304px; top: 66px; }
  .identity__name { color: var(--blue); font-size: 20px; font-weight: 500; letter-spacing: 1px; text-transform: uppercase; line-height: 24px; }
  .identity__title { color: var(--white); font-size: 13px; font-weight: 500; letter-spacing: 1.5px; text-transform: uppercase; margin-top: 2px; }

  .brand { position: absolute; left: 318px; top: 150px; display: flex; align-items: center; gap: 10px; }
  .brand__mark { width: 18px; height: 18px; background: var(--blue); }
  .brand__name { color: var(--blue); font-size: 34px; font-weight: 600; letter-spacing: .5px; }

  .contact { position: absolute; left: 46px; top: 150px; color: var(--grey); font-size: 11.5px; line-height: 19px; }
  .contact__address { color: var(--grey-dim); margin-bottom: 8px; }
  .contact__row { display: flex; align-items: center; gap: 8px; color: var(--white); }
  .contact__row svg { width: 11px; height: 11px; fill: var(--blue); flex: none; }

  .back-brand { position: absolute; inset: 0; display: flex; align-items: center; justify-content: center; gap: 14px; }
  .back-brand__mark { width: 30px; height: 30px; background: var(--blue); }
  .back-brand__name { color: var(--blue); font-size: 44px; font-weight: 600; }
</style>
</head>
<body>
  <section class="card card--front">
    <div class="card__frame"></div>
    <div class="band"></div>
    <div class="tab"></div>

    <div class="identity">
      <div class="identity__name">Malcolm Tudd</div>
      <div class="identity__title">General Manager</div>
    </div>

    <div class="brand">
      <span class="brand__mark"></span>
      <span class="brand__name">vextorial</span>
    </div>

    <div class="contact">
      <p class="contact__address">42 Harbor Lane<br>Suite 210 Dockside Park</p>
      <p class="contact__row">
        <svg viewBox="0 0 24 24"><path d="M6.6 10.8a15 15 0 0 0 6.6 6.6l2.2-2.2c.3-.3.7-.4 1-.2 1.1.4 2.3.6 3.6.6.6 0 1 .4 1 1V20c0 .6-.4 1-1 1A17 17 0 0 1 3 4c0-.6.4-1 1-1h3.5c.6 0 1 .4 1 1 0 1.3.2 2.5.6 3.6.1.3 0 .7-.2 1z"/></svg>
        1 877 555 0143
      </p>
      <p class="contact__row">
        <svg viewBox="0 0 24 24"><path d="M7 2h10a2 2 0 0 1 2 2v16a2 2 0 0 1-2 2H7a2 2 0 0 1-2-2V4a2 2 0 0 1 2-2zm0 3v13h10V5z"/></svg>
        1 519 555 0172
      </p>
      <p class="contact__row">
        <svg viewBox="0 0 24 24"><path d="M2 5h20v14H2zm2 2v.5l8 5 8-5V7z"/></svg>
        malcolm@vextorial.com
      </p>
      <p class="contact__row">
        <svg viewBox="0 0 24 24"><circle cx="12" cy="12" r="10"/></svg>
        www.vextorial.com
      </p>
    </div>
  </section>

  <section class="card card--back">
    <div class="card__frame"></div>
    <div class="back-brand">
      <span class="back-brand__mark"></span>
      <span class="back-brand__name">vextorial</span>
    </div>
  </section>
</body>
</html>
```